Fundraising Study Day East of England. Lift the January blues!

A flyer to advertise a fundraising event of lectures for dental hygienists and therapists in support of the exemption campaign. Currently dental hygienists and therapists require a prescription to deliver certain treatment or recommend certain toothpastes. If we are successful in the campaign we will be able to treat patients without these restrictions.

Industry/Entity Type

Dental

```html
<!DOCTYPE html>
<html lang="en">
<head>
<meta charset="utf-8">
<title>Fundraising Study Day East of England</title>
<link href="https://fonts.googleapis.com/css2?family=Roboto+Condensed:wght@400;700&family=Open+Sans:wght@400;600;700&display=swap" rel="stylesheet">
<style>
:root{
  --teal:#1ba493;
  --teal-light:#8fd6c8;
  --teal-pale:#b9e6dc;
  --slate:#5e5f61;
  --ink:#3a3a3a;
  --white:#ffffff;
}
*{margin:0;padding:0;box-sizing:border-box}
html,body{width:929px;height:1200px;overflow:hidden;background:var(--white)}
.flyer{position:relative;width:929px;height:1200px;overflow:hidden;font-family:"Open Sans",sans-serif;color:var(--ink)}
.hero-photo{position:absolute;left:0;top:0;width:929px;height:380px;background:linear-gradient(160deg,#dfe7ee 0%,#b7c8d8 35%,#3f78b8 60%,#2c5f9e 100%)}
.title-band{position:absolute;left:0;top:340px;width:929px;height:150px}
.title{position:absolute;left:48px;top:378px;font-family:"Roboto Condensed",sans-serif;font-weight:700;font-size:45px;color:var(--white);letter-spacing:.2px;white-space:nowrap}
.subtitle{position:absolute;left:48px;top:437px;font-family:"Roboto Condensed",sans-serif;font-weight:400;font-size:35px;color:var(--white);white-space:nowrap}
.intro{position:absolute;left:30px;top:505px;width:600px;text-align:center;font-size:14.6px;line-height:20px;color:var(--ink)}
.intro h2{font-size:19px;color:var(--teal);font-weight:700;margin-bottom:2px}
.intro strong{color:var(--teal);font-weight:700}
.details{position:absolute;left:667px;top:480px;width:220px;font-weight:700;font-size:15.5px;line-height:20px;color:var(--ink)}
.details .block{padding:0 0 10px;border-bottom:1px solid #bfbfbf;margin-bottom:10px}
.details .cost{color:var(--teal);border-bottom:2px solid var(--teal);padding-bottom:6px;display:inline-block;width:160px}
.spine{position:absolute;left:68px;top:660px;width:80px;height:420px;background:var(--teal-pale)}
.session{position:absolute;left:68px;height:60px;display:flex}
.session .num{width:92px;background:var(--teal);color:var(--white);font-family:"Roboto Condensed",sans-serif;font-weight:700;font-size:46px;display:flex;align-items:center;justify-content:center;clip-path:polygon(0 0,100% 0,100% 100%,18% 100%,0 80%)}
.session .speaker{width:180px;background:var(--teal-light);font-family:"Roboto Condensed",sans-serif;font-weight:700;font-size:17px;color:#2f3a3a;display:flex;flex-direction:column;justify-content:center;text-align:center;line-height:18px}
.session .speaker span{display:block;font-family:"Open Sans",sans-serif;font-weight:400;font-size:14px;color:#333;margin-top:3px;line-height:16px}
.session .topic{width:490px;background:var(--slate);color:var(--white);font-size:14.6px;line-height:19px;padding:6px 14px;border-radius:0 14px 14px 0;display:flex;align-items:center}
.session .topic.small{font-size:11.4px;line-height:14px}
.break{position:absolute;left:353px;top:896px;font-weight:700;font-size:15px;line-height:20px;color:var(--teal)}
.footer{position:absolute;left:0;top:1075px;width:929px;height:125px}
.more{position:absolute;left:58px;top:1110px;color:var(--white);font-size:22px;white-space:nowrap}
.share{position:absolute;left:530px;top:1104px;color:var(--white);font-size:19px;display:flex;align-items:center;gap:8px;white-space:nowrap}
.share .networks{font-size:12px;font-weight:400}
.url{position:absolute;left:58px;top:1141px;color:var(--white);font-size:14.4px;white-space:nowrap}
</style>
</head>
<body>
<div class="flyer">
  <div class="hero-photo" role="img" aria-label="Photo of a cheerful dental team in blue scrubs joining hands in a clinic"></div>

  <svg class="title-band" viewBox="0 0 929 150" aria-hidden="true">
    <polygon fill="#1ba493" points="0,22 60,14 130,20 210,8 300,18 380,10 470,20 560,6 650,16 740,8 830,18 929,10 929,128 860,134 780,126 700,136 620,128 540,138 470,130 380,140 300,130 220,138 140,128 60,136 0,130"/>
  </svg>
  <h1 class="title">FUNDRAISING STUDY DAY EAST OF ENGLAND</h1>
  <p class="subtitle">Lift the January blues!</p>

  <section class="intro">
    <h2>Come Join us</h2>
    <p>A fundraising event to <strong>support our exemptions project</strong>.<br>
    The day will consist of a series of presentations ranging from<br>
    <strong>the new ECPD to new technologies</strong>.<br>
    The aim, being to enhance our learning and raise funds to support the<br>
    exemptions campaign. The speaker line includes some of the<br>
    <strong>UK and Irelands most respected dental professionals in our field.</strong></p>
  </section>

  <aside class="details">
    <div class="block">LOCATION:<br>Larkfield Hotel Orbit Way<br>Hatfield AL10 4XR</div>
    <div>DATE AND TIME<br>Fri 19 January 2018<br>09:00 – 16:30 GMT</div>
    <div style="margin-top:12px"><span class="cost">Cost - £101.48</span></div>
  </aside>

  <div class="spine"></div>

  <div class="session" style="top:667px">
    <div class="num">1</div>
    <div class="speaker">Fiona Marlow<span>9.30 - 10.15</span></div>
    <div class="topic">Immediate past president of the ADHT will be updating us on all things ECPD</div>
  </div>
  <div class="session" style="top:751px">
    <div class="num">2</div>
    <div class="speaker">Megan Ashdown<span>10.15 - 11.00</span></div>
    <div class="topic">Will provide an update on teeth whiteing and explain how social media has impacted her business</div>
  </div>
  <div class="session" style="top:830px;height:63px">
    <div class="num">3</div>
    <div class="speaker">Juliette Carrow<span>10.15 - 11.00<br>&amp; 15.30 -16.30</span></div>
    <div class="topic">Our internationally acclaimed speaker will update our knowledge of periodontal disease and nutrition and new technologies.</div>
  </div>
  <p class="break">11.00 - 11.30 Break</p>
  <div class="session" style="top:920px;height:62px">
    <div class="num">4</div>
    <div class="speaker">Siobhan Dalby<br>&amp; Melonie Thorne<span>11.30 - 13.00</span></div>
    <div class="topic small">Will be providing a combined presentation on 'Scaling your business' and start to finish Sonaflow techniques. The aim being to build our business with effective communications, systems and protocols. This sessions promises audience participation!</div>
  </div>
  <div class="session" style="top:1000px">
    <div class="num">5</div>
    <div class="speaker">Pat Kendrew<span>14 - 15.00</span></div>
    <div class="topic">Save your back. All things posture.</div>
  </div>

  <svg class="footer" viewBox="0 0 929 125" aria-hidden="true">
    <polygon fill="#1ba493" points="0,14 80,6 170,16 260,4 350,14 440,6 530,16 620,4 710,14 800,6 929,12 929,125 0,125"/>
  </svg>
  <p class="more">For more details visit:</p>
  <div class="share">Share with with friends <span class="networks">Pagebook · Chirper · Linkwork</span></div>
  <p class="url">www.ticketfold.co.uk/e/fundraising-study-day-east-of-england-lift-the-january-blues-tickets-4829305</p>
</div>
</body>
</html>
```